Amber Heron Fund Pitch Deck

This is a PowerPoint for use in investor presentations. The copy is written (although it may have small tweaks) and the designer will be responsible for creating a template and some graphical representations inside the presentation.

Note on the logo. Only the Amber Heron should be used, not the text.

```html
<!DOCTYPE html>
<html lang="en">
<head>
<meta charset="utf-8">
<title>Amber Heron Fund Pitch Deck</title>
<link href="https://fonts.googleapis.com/css2?family=Lato:wght@400;700;900&display=swap" rel="stylesheet">
<style>
:root{
  --page:#e9eaec;
  --paper:#ffffff;
  --navy:#1f3a6e;
  --blue:#4a78cf;
  --blue-soft:#9db6e6;
  --ink:#4a4f58;
  --muted:#8c9098;
  --rule:#d5d9e0;
  --photo-a:#b9c2cd;
  --photo-b:#e2e6eb;
}
*{box-sizing:border-box;margin:0;padding:0}
html,body{width:742px;height:1200px;overflow:hidden}
body{position:relative;background:var(--page);font-family:'Lato',Arial,sans-serif;color:var(--ink)}
.page-heading,.zoom-note{position:absolute;left:0;width:742px;text-align:center;color:#5b5f66;letter-spacing:2px;font-size:13px}
.page-heading{top:18px}
.zoom-note{top:520px;font-size:12px}
.slide{position:absolute;background:var(--paper);overflow:hidden;box-shadow:0 3px 10px rgba(0,0,0,.12)}
.slide-sm{width:336px;height:190px}
.col-l{left:26px}.col-r{left:380px}
.row-1{top:560px}.row-2{top:770px}.row-3{top:980px}
.footer-band{position:absolute;left:0;right:0;bottom:0;height:7px;background:linear-gradient(90deg,var(--blue),var(--navy))}
.page-no{position:absolute;right:10px;bottom:10px;font-size:5px;color:var(--muted)}
.brand{position:absolute;left:12px;top:10px;display:flex;align-items:center;gap:5px;font-weight:900;font-size:11px;color:var(--navy);letter-spacing:.3px}
.brand-mark{width:9px;height:9px;background:var(--blue)}
.section-label{position:absolute;left:12px;top:26px;font-size:6px;color:var(--blue);font-weight:700}
.body-copy{font-size:4.6px;line-height:1.45;color:var(--ink)}
.photo{position:absolute;background:linear-gradient(135deg,var(--photo-a),var(--photo-b))}
/* title slide */
.title-slide{left:71px;top:100px;width:600px;height:338px}
.title-slide .photo{left:0;top:0;width:600px;height:190px}
.brush-band{position:absolute;left:60px;top:150px;width:480px;height:70px;background:linear-gradient(90deg,rgba(74,120,207,.2),var(--blue) 40%,rgba(74,120,207,.6));border-radius:40px 10px 50px 8px}
.title-main{position:absolute;top:236px;width:100%;text-align:center;font-weight:900;font-size:32px;color:var(--navy);letter-spacing:1px}
.title-url{position:absolute;top:278px;width:100%;text-align:center;font-size:11px;letter-spacing:4px;color:var(--muted)}
/* team rows */
.person{position:absolute;left:12px;width:312px;display:flex;gap:8px}
.person .photo{position:static;width:30px;height:34px;flex:none;background:linear-gradient(160deg,#c9cdd3,#eef0f3)}
.person h4{font-size:5px;color:var(--blue);margin-bottom:2px}
/* stats */
.stat{position:absolute;top:44px;width:96px;font-size:5.5px;line-height:1.3;color:var(--navy)}
.stat b{display:block;font-size:11px;font-weight:900;color:var(--blue)}
.source-bar{position:absolute;left:12px;right:12px;top:110px;height:13px;background:var(--blue-soft);font-size:5px;color:var(--navy);padding:4px 6px}
</style>
</head>
<body>

<div class="page-heading">POWERPOINT TEMPLATE</div>

<section class="slide title-slide">
  <div class="photo" role="img" aria-label="Photo of a business meeting in a bright office"></div>
  <div class="brush-band" role="img" aria-label="Blue painted brush stroke decoration"></div>
  <div class="title-main">PRESENTATION TITLE</div>
  <div class="title-url">www.amberheronfund.com</div>
  <div class="footer-band"></div>
</section>

<div class="zoom-note">CLICK ZOOM TO SEE DETAILS</div>

<!-- title slide small -->
<section class="slide slide-sm col-l row-1">
  <div class="photo" style="left:0;top:0;width:336px;height:105px" role="img" aria-label="Photo of a business meeting"></div>
  <div class="brush-band" style="left:34px;top:84px;width:268px;height:38px"></div>
  <div class="title-main" style="top:130px;font-size:17px">PRESENTATION TITLE</div>
  <div class="title-url" style="top:153px;font-size:6px;letter-spacing:2px">www.amberheronfund.com</div>
  <div class="footer-band"></div>
</section>

<!-- the deal -->
<section class="slide slide-sm col-r row-1">
  <div class="brand"><span class="brand-mark"></span>AMBER HERON NPL FUND</div>
  <div class="section-label">01 The Deal</div>
  <p class="body-copy" style="position:absolute;left:12px;top:38px;width:312px">The fund acquires non-performing commercial loans at a discount and works each asset toward recovery, restructure or sale to build steady returns for partners.</p>
  <p class="body-copy" style="position:absolute;left:12px;top:62px;width:312px">Each loan is reviewed by our team before purchase, with a clear plan for collateral, timing and exit in every case.</p>
  <p class="body-copy" style="position:absolute;left:12px;top:100px;width:150px">We focus on small and mid-size loans where larger buyers do not compete, giving the fund better pricing and more control.</p>
  <div class="photo" style="left:176px;top:96px;width:148px;height:68px" role="img" aria-label="Photo of a team reviewing documents at a desk"></div>
  <span class="page-no">2</span>
  <div class="footer-band"></div>
</section>

<!-- the team -->
<section class="slide slide-sm col-l row-2">
  <div class="brand"><span class="brand-mark"></span>AMBER HERON NPL FUND</div>
  <div class="section-label">02 The Team</div>
  <div class="person" style="top:42px"><div class="photo" role="img" aria-label="Portrait of a team member"></div><div><h4>Managing Partner – Loan Acquisition</h4><p class="body-copy">Twenty years in commercial lending and loan workouts, with deep ties to regional banks and servicers.</p></div></div>
  <div class="person" style="top:100px"><div class="photo" role="img" aria-label="Portrait of a team member"></div><div><h4>Partner – Asset Management</h4><p class="body-copy">Leads recovery strategy and has resolved hundreds of distressed loans across many property types.</p></div></div>
  <span class="page-no">3</span>
  <div class="footer-band"></div>
</section>

<!-- the people -->
<section class="slide slide-sm col-r row-2">
  <div class="brand"><span class="brand-mark"></span>AMBER HERON NPL FUND</div>
  <div class="section-label">02 The People</div>
  <div class="person" style="top:42px;width:150px"><div class="photo" role="img" aria-label="Portrait of a team member"></div><div><h4>Partner – Investor Relations</h4><p class="body-copy">Keeps partners informed with clear quarterly reports.</p></div></div>
  <div class="person" style="top:42px;left:174px;width:150px"><div class="photo" role="img" aria-label="Portrait of a team member"></div><div><h4>Partner – Legal</h4><p class="body-copy">Guides each loan through title and court steps.</p></div></div>
  <p class="body-copy" style="position:absolute;left:12px;top:96px;width:312px">Together the team brings lending, legal and property skills under one roof, so every asset is handled from purchase to exit with care.</p>
  <span class="page-no">4</span>
  <div class="footer-band"></div>
</section>

<!-- market stats -->
<section class="slide slide-sm col-l row-3">
  <div class="brand"><span class="brand-mark"></span>AMBER HERON NPL FUND</div>
  <div class="stat" style="left:12px">The commercial lending market was valued at <b>$1,823.5</b> billion in 2016</div>
  <div class="stat" style="left:120px">Projected to reach <b>$29,279.8</b> billion by 2025</div>
  <div class="stat" style="left:228px">Growing at a CAGR of <b>13.1%</b> from 2017 to 2025</div>
  <div class="source-bar">Source: www.marketstudy-example.com/commercial-lending-report</div>
  <p class="body-copy" style="position:absolute;left:12px;top:134px;width:312px;font-size:5px">The credit cycle is entering a period of rising interest rates and defaults. The fund seeks to take advantage of this emerging opportunity.</p>
  <span class="page-no">5</span>
  <div class="footer-band"></div>
</section>

<!-- process -->
<section class="slide slide-sm col-r row-3">
  <div class="brand"><span class="brand-mark"></span>AMBER HERON NPL FUND</div>
  <div class="section-label">04 The Process</div>
  <svg width="336" height="190" style="position:absolute;left:0;top:0" font-family="Lato, Arial, sans-serif">
    <line x1="24" y1="46" x2="312" y2="46" stroke="var(--blue-soft)" stroke-width="2"/>
    <g fill="var(--blue)" font-size="6" font-weight="700" text-anchor="middle">
      <circle cx="24" cy="46" r="6"/><circle cx="65" cy="46" r="6"/><circle cx="106" cy="46" r="6"/><circle cx="147" cy="46" r="6"/>
      <circle cx="188" cy="46" r="6"/><circle cx="229" cy="46" r="6"/><circle cx="270" cy="46" r="6"/><circle cx="311" cy="46" r="6"/>
      <g fill="#fff"><text x="24" y="48">A</text><text x="65" y="48">B</text><text x="106" y="48">C</text><text x="147" y="48">D</text><text x="188" y="48">E</text><text x="229" y="48">F</text><text x="270" y="48">G</text><text x="311" y="48">H</text></g>
    </g>
    <g fill="var(--blue)">
      <rect x="14" y="68" width="60" height="30" rx="3"/><rect x="96" y="68" width="60" height="30" rx="3"/>
      <rect x="178" y="68" width="60" height="30" rx="3"/><rect x="260" y="68" width="60" height="30" rx="3"/>
      <rect x="55" y="114" width="60" height="30" rx="3"/><rect x="137" y="114" width="60" height="30" rx="3"/>
      <rect x="219" y="114" width="60" height="30" rx="3"/>
    </g>
    <g stroke="var(--navy)" stroke-width="1.2" fill="none">
      <path d="M74 83h20M156 83h20M238 83h20M290 98v8h-195v6M115 129h20M197 129h20"/>
    </g>
    <g fill="#fff" font-size="4.6" text-anchor="middle">
      <text x="44" y="85">Source loans</text><text x="126" y="85">Review assets</text><text x="208" y="85">Price and bid</text><text x="290" y="85">Close purchase</text>
      <text x="85" y="131">Work out plan</text><text x="167" y="131">Recover value</text><text x="249" y="131">Exit and return</text>
    </g>
    <text x="12" y="162" font-size="4.6" fill="var(--ink)">Each step is tracked and reported so partners can follow every loan from purchase to exit.</text>
  </svg>
  <span class="page-no">6</span>
  <div class="footer-band"></div>
</section>

</body>
</html>
```